business card, letterhead, and envelope design for mobile ultrasound imaging
Corvane Sonography Partners, LLC
Simple
Maren Tocks BS, RDMS, RVT
Managing Partner
6184 County Road 41S
Defuniak Springs, FL 32433
P.O. Box 7126
Niceville, FL 32578-7126
marentocks@corvanesono.example
www.corvanesono.example

```html
<!DOCTYPE html>
<html lang="en">
<head>
<meta charset="utf-8">
<title>Corvane Sonography Partners – Stationery</title>
<link href="https://fonts.googleapis.com/css2?family=Lato:wght@400;700&display=swap" rel="stylesheet">
<style>
  :root {
    --backdrop: #9c6236;
    --paper: #ffffff;
    --brand-blue: #1d6db3;
    --brand-green: #8cc63f;
    --ink: #4a4a4a;
    --ink-soft: #8a8a8a;
    --rule: #dcdcdc;
  }
  * { box-sizing: border-box; margin: 0; padding: 0; }
  html, body { width: 1200px; height: 490px; overflow: hidden; }
  body {
    background: var(--backdrop);
    font-family: "Lato", Arial, sans-serif;
    color: var(--ink);
    position: relative;
  }
  .sheet {
    position: absolute;
    background: var(--paper);
    box-shadow: 0 3px 8px rgba(0,0,0,.35);
    overflow: hidden;
  }
  .brand {
    display: flex; align-items: center; gap: 5px;
    color: var(--brand-blue); font-weight: 700; line-height: 1.1;
    white-space: nowrap;
  }
  .brand-dot { border-radius: 50%; background: var(--brand-green); flex: none; }
  .contact { display: flex; align-items: center; gap: 3px; white-space: nowrap; }
  .contact svg { flex: none; }

  /* Letterhead */
  .letterhead { left: 53px; top: 36px; width: 206px; height: 420px; }
  .letterhead .brand { position: absolute; top: 16px; left: 0; right: 0; justify-content: center; font-size: 7.5px; }
  .letterhead .brand-dot { width: 10px; height: 10px; }
  .letter-body { position: absolute; left: 18px; right: 18px; top: 56px; font-size: 4.6px; line-height: 1.55; }
  .letter-body p { margin-bottom: 7px; text-align: justify; }
  .letter-sign { width: 38px; border-top: 0.6px solid var(--ink-soft); margin-top: 12px; }
  .letter-footer {
    position: absolute; left: 18px; right: 18px; bottom: 14px;
    border-top: 0.6px solid var(--rule); padding-top: 6px;
    display: grid; grid-template-columns: 1.25fr 1fr; gap: 3px 6px;
    font-size: 3.9px; color: var(--ink-soft);
  }

  /* Envelope back */
  .envelope-back { left: 300px; top: 101px; width: 415px; height: 158px; }
  .envelope-back svg.flap { position: absolute; inset: 0; }
  .envelope-back .brand { position: absolute; top: 16px; left: 0; right: 0; justify-content: center; font-size: 6px; }
  .envelope-back .brand-dot { width: 8px; height: 8px; }

  /* Envelope front */
  .envelope-front { left: 300px; top: 288px; width: 415px; height: 168px; }
  .envelope-front .brand { position: absolute; left: 14px; top: 14px; font-size: 7px; }
  .envelope-front .brand-dot { width: 10px; height: 10px; }
  .return-address { position: absolute; left: 14px; top: 34px; font-size: 4.4px; color: var(--ink-soft); line-height: 1.5; }

  /* Card front */
  .card-front { left: 761px; top: 101px; width: 367px; height: 158px; }
  .card-front .brand { position: absolute; left: 0; right: 0; top: 68px; justify-content: center; font-size: 15px; gap: 7px; }
  .card-front .brand-dot { width: 20px; height: 20px; }

  /* Card back */
  .card-back { left: 761px; top: 288px; width: 367px; height: 168px; }
  .holder { position: absolute; left: 126px; top: 22px; }
  .holder-name { font-size: 8px; font-weight: 700; color: var(--brand-blue); }
  .holder-title { font-size: 5.5px; color: var(--ink-soft); margin-top: 2px; }
  .holder-address { position: absolute; left: 126px; top: 70px; font-size: 5px; line-height: 1.55; }
  .holder-contacts { position: absolute; left: 232px; top: 68px; font-size: 5px; display: grid; gap: 4px; }
  .holder-contacts .contact { border-bottom: 0.6px solid var(--brand-blue); padding-bottom: 2px; }
</style>
</head>
<body>

  <section class="sheet letterhead" aria-label="Letterhead">
    <div class="brand"><span class="brand-dot"></span><span>Corvane Sonography Partners, LLC</span></div>
    <div class="letter-body">
      <p>Dear client, thank you for choosing our mobile imaging team. We bring certified sonographers and modern equipment directly to your clinic, hospital or care facility on schedule.</p>
      <p>Each study is performed with care and reviewed for quality before results are delivered to your physicians. Our reports arrive quickly so patient care continues without delay.</p>
      <p>We offer vascular, abdominal, obstetric and cardiac exams, with flexible hours that suit your staff and your patients.</p>
      <p>Please contact our office to arrange a visit or to discuss your imaging needs in more detail.</p>
      <p>Sincerely,</p>
      <div class="letter-sign"></div>
    </div>
    <div class="letter-footer">
      <span class="contact"><svg width="5" height="5" viewBox="0 0 10 10"><circle cx="5" cy="5" r="5" fill="var(--brand-green)"/></svg>6184 County Road 41S, Defuniak Springs, FL 32433</span>
      <span class="contact"><svg width="5" height="5" viewBox="0 0 10 10"><circle cx="5" cy="5" r="5" fill="var(--brand-blue)"/></svg>marentocks@corvanesono.example</span>
      <span class="contact"><svg width="5" height="5" viewBox="0 0 10 10"><circle cx="5" cy="5" r="5" fill="var(--brand-green)"/></svg>(850) 555-0142</span>
      <span class="contact"><svg width="5" height="5" viewBox="0 0 10 10"><circle cx="5" cy="5" r="5" fill="var(--brand-blue)"/></svg>www.corvanesono.example</span>
    </div>
  </section>

  <section class="sheet envelope-back" aria-label="Envelope back">
    <svg class="flap" width="415" height="158" viewBox="0 0 415 158">
      <polyline points="0,0 207,70 415,0" fill="none" stroke="var(--rule)" stroke-width="1"/>
      <line x1="0" y1="158" x2="150" y2="70" stroke="var(--rule)" stroke-width="1"/>
      <line x1="415" y1="158" x2="265" y2="70" stroke="var(--rule)" stroke-width="1"/>
    </svg>
    <div class="brand"><span class="brand-dot"></span><span>Corvane Sonography Partners, LLC</span></div>
  </section>

  <section class="sheet envelope-front" aria-label="Envelope front">
    <div class="brand"><span class="brand-dot"></span><span>Corvane Sonography Partners, LLC</span></div>
    <div class="return-address">
      6184 County Road 41S, Defuniak Springs, FL 32433<br>
      P.O. Box 7126, Niceville, FL 32578-7126
    </div>
  </section>

  <section class="sheet card-front" aria-label="Business card front">
    <div class="brand"><span class="brand-dot"></span><span>Corvane Sonography Partners, LLC</span></div>
  </section>

  <section class="sheet card-back" aria-label="Business card back">
    <div class="holder">
      <div class="holder-name">Maren Tocks BS, RDMS, RVT</div>
      <div class="holder-title">Managing Partner</div>
    </div>
    <div class="holder-address">
      6184 County Road 41S<br>
      Defuniak Springs, FL 32433<br>
      P.O. Box 7126<br>
      Niceville, FL 32578-7126
    </div>
    <div class="holder-contacts">
      <span class="contact"><svg width="6" height="6" viewBox="0 0 10 10"><circle cx="5" cy="5" r="5" fill="var(--brand-green)"/></svg>marentocks@corvanesono.example</span>
      <span class="contact"><svg width="6" height="6" viewBox="0 0 10 10"><circle cx="5" cy="5" r="5" fill="var(--brand-blue)"/></svg>www.corvanesono.example</span>
      <span class="contact"><svg width="6" height="6" viewBox="0 0 10 10"><circle cx="5" cy="5" r="5" fill="var(--brand-green)"/></svg>(850) 555-0142</span>
      <span class="contact"><svg width="6" height="6" viewBox="0 0 10 10"><circle cx="5" cy="5" r="5" fill="var(--brand-blue)"/></svg>(850) 555-0187</span>
    </div>
  </section>

</body>
</html>
```